Drowning Victims Recovery Website Design

We are working with Tidewell Search Dive Team. They provide recovery services for drowning victims so they can be reunited with their loved ones.

Some sites to use for inspiration:

https://shelterbrookvale.org
https://www.gallantascent.org
https://www.kindspringfund.org
https://www.tellano.ca/en

Thank you for taking the time to consider designing a website for us. We are web developers based in Stockton, CA, USA. Most of our projects go through the same process. Understanding this process may help you win a project with us. We custom-code all of our websites in-house. We don’t have any requirements as to what tools you use for your design, but we prefer Figma files. For any design that we label as four-stars, we send it to the client for review. The client picks the final design they want us to use. Once we complete this process, we will continue to show additional clients all the four-star sites and purchase them later. Your designs will have multiple chances to sell. For better chances of success, we ask that you follow these guidelines.

IMAGES:
If you use any images or icons in the design, we ask that you have a link to the asset so we can purchase the image/icon. Most of the designs we submit do not have the customer’s images on them unless they have some great images. Be creative; show us the feeling you are trying to portray with your image choices. Use any royalty-free site you choose. We subscribe to Quillmark and mainly use their images, but we can purchase images outside of Quillmark.

PLEASE NOTE: we will not submit designs to clients with watermarks on the images.

FONTS:
We ask that you identify the fonts used in the design. This can be done in a message if you want. We typically use Zintro Fonts and Quillmark Fonts.

CONTENT:
We're always open to different content and ideas. We often submit designs with stock images so the client can see our vision. We typically take pictures after the website launch to use their images with our vision. Lorem Ipsum is fine for paragraphs, but we ask that you write the headers in correct English. We want to be able to show the vision and identify the sections of the website.

INSPIRATION:
We typically add a couple of links in the brief of websites we like to help you get started in your design.

REVISIONS:
We do not often ask for revisions of the designs unless we see something in the design that may not appeal to the client. If there are slight changes that we want to make, we do that in the development process.

FEEDBACK:
We rarely give feedback on designs during the design process. We are working on many website projects and do not have the time to provide feedback. We usually respond if your request is well thought out and asks specific questions, but a note asking “feedback, please” usually goes unanswered.

```html
<!DOCTYPE html>
<html lang="en">
<head>
<meta charset="utf-8">
<title>Tidewell Search Dive Team</title>
<link href="https://fonts.googleapis.com/css2?family=Roboto:wght@400;500;700;900&family=Open+Sans:wght@400;600;700&display=swap" rel="stylesheet">
<style>
:root{
  --red:#c1080f;
  --red-dark:#8e0509;
  --blue:#1d4d7c;
  --blue-dark:#123557;
  --navy:#0c2643;
  --ink:#222;
  --muted:#555;
  --light:#eef1f4;
  --white:#fff;
}
*{box-sizing:border-box;margin:0;padding:0}
html,body{width:1200px;height:4789px;overflow:hidden}
body{position:relative;font-family:"Open Sans",sans-serif;color:var(--ink);background:var(--white)}
h1,h2,h3,h4{font-family:"Roboto",sans-serif}
.abs{position:absolute}
.btn{position:absolute;display:flex;align-items:center;justify-content:center;border-radius:22px;font-family:"Roboto",sans-serif;font-weight:700;font-size:14px;color:var(--white);text-decoration:none}
.btn-red{background:var(--red)}
.btn-black{background:#0b0b0b}
.btn-outline{border:2px solid var(--white)}
.divider{position:absolute;left:495px;width:210px;height:2px;background:var(--red)}
.divider::after{content:"";position:absolute;left:99px;top:-6px;width:12px;height:12px;background:var(--red);transform:rotate(45deg)}
.section-title{position:absolute;left:0;width:1200px;text-align:center;font-size:38px;font-weight:700;color:var(--blue)}
.section-title .hl{color:var(--red)}
.placeholder{position:absolute}

/* header */
.site-header{position:absolute;top:0;left:0;width:1200px;height:108px;background:var(--white)}
.brand{position:absolute;left:140px;top:28px;display:flex;align-items:center;gap:10px;font-family:"Roboto",sans-serif;font-weight:900;font-size:24px;color:var(--red);line-height:1}
.brand .dot{width:14px;height:14px;background:var(--red);border-radius:50%}
.brand small{display:block;font-size:12px;font-weight:500;color:var(--blue);letter-spacing:1px;margin-top:4px}
.main-nav{position:absolute;left:347px;top:42px;display:flex;gap:0}
.main-nav a{font-size:15px;color:var(--ink);text-decoration:none;margin-right:32px}
.main-nav a.active{color:var(--red);font-weight:700}

/* hero */
.hero{position:absolute;top:108px;left:0;width:1200px;height:540px}
.hero-text{position:absolute;left:190px;top:130px;color:var(--white)}
.hero-text h1{font-size:40px;line-height:46px;font-weight:700}
.hero-text h1 .hl{color:var(--red)}
.hero-text p{margin-top:14px;font-size:18px;line-height:24px}
.scroll-btn{position:absolute;left:572px;top:620px;width:56px;height:56px;border-radius:50%;background:var(--white);border:3px solid var(--blue-dark);display:flex;align-items:center;justify-content:center}

/* about */
.about-bg{position:absolute;top:640px;left:0;width:1200px;height:1360px;background:linear-gradient(90deg,#f6d9d9 0%,#fbf1f1 30%,#ffffff 55%,#e8eef3 100%)}
.about-title{position:absolute;left:613px;top:725px;font-size:38px;line-height:46px;font-weight:700;color:var(--blue)}
.about-title .hl{color:var(--red)}
.about-line{position:absolute;left:1012px;top:758px;width:188px;height:2px;background:var(--red)}
.about-line::before{content:"";position:absolute;left:-4px;top:-6px;width:12px;height:12px;background:var(--red);transform:rotate(45deg)}
.about-text{position:absolute;left:613px;top:830px;width:450px;font-size:14px;line-height:29px;color:var(--ink)}

/* stages */
.stage{position:absolute;top:1304px;width:168px;text-align:center}
.stage .ring{width:168px;height:168px;border-radius:50%;border:6px solid var(--red);padding:8px}
.stage .ring div{width:100%;height:100%;border-radius:50%;background:var(--red);display:flex;align-items:center;justify-content:center}
.stage h4{margin-top:16px;color:var(--red);font-size:20px;line-height:25px;font-weight:700}
.stage-dash{position:absolute;top:1387px;height:0;border-top:2px dashed var(--red)}
.team-type{position:absolute;top:1618px;width:400px}
.team-type h3{color:var(--red);font-size:20px;font-weight:700}
.team-type p{margin-top:14px;font-size:13px;line-height:17px;color:var(--muted)}

/* services */
.services-band{position:absolute;top:2000px;left:0;width:1200px;height:568px;background:#e6e8ea}
.services-list{position:absolute;left:145px;top:2125px;width:410px;color:var(--white)}
.service-item{position:relative;padding-left:37px;margin-bottom:20px}
.service-item .plus{position:absolute;left:0;top:4px;width:20px;height:20px;border-radius:50%;background:var(--red);color:var(--white);font-weight:700;font-size:16px;line-height:20px;text-align:center}
.service-item h3{font-size:20px;font-weight:700}
.service-item p{margin-top:8px;font-size:13.5px;line-height:24px}
.services-heading{position:absolute;left:613px;top:2002px;color:var(--red);font-size:38px;font-weight:700;line-height:44px}
.services-heading small{display:block;color:var(--blue);font-size:29px;font-weight:500;line-height:36px}

/* team */
.team-band{position:absolute;top:2568px;left:0;width:1200px;height:387px;background:var(--red)}
.team-card{position:absolute;top:2752px;width:217px;height:295px;border-radius:6px;overflow:hidden;box-shadow:0 8px 18px rgba(0,0,0,.18)}
.team-label{position:absolute;left:8px;right:8px;bottom:8px;height:82px;background:var(--red);border-radius:4px;color:var(--white);padding:22px 16px}
.team-label h4{font-size:17px;font-weight:700}
.team-label p{font-size:11px;margin-top:2px}
.team-dots{position:absolute;top:3089px;left:558px;display:flex;gap:6px}
.team-dots span{height:4px;width:14px;background:var(--red)}
.team-dots span:first-child{width:32px}

/* reuniting */
.reunite-title{position:absolute;left:142px;top:3148px;color:var(--red);font-size:38px;font-weight:700;line-height:40px}
.reunite-title small{display:block;color:var(--blue);font-size:30px;font-weight:700;line-height:36px}
.reunite-line{position:absolute;left:0;top:3235px;width:118px;height:2px;background:var(--red)}
.reunite-line::after{content:"";position:absolute;right:-4px;top:-6px;width:12px;height:12px;background:var(--red);transform:rotate(45deg)}
.reunite-text{position:absolute;left:142px;top:3262px;width:200px;font-size:12px;line-height:19px;color:var(--muted)}
.info-card{position:absolute;top:3160px;width:329px;height:240px;border-radius:10px;overflow:hidden;color:var(--white)}
.info-card .copy{position:absolute;left:28px;right:24px}
.info-card h3{font-size:22px;font-weight:700}
.info-card p{margin-top:8px;font-size:11.5px;line-height:19px}

/* prevention banner */
.prevent{position:absolute;top:3483px;left:138px;width:924px;height:205px;border-radius:4px;overflow:hidden;color:var(--white)}
.prevent h3{position:absolute;left:42px;top:45px;font-size:24px;font-weight:700}
.prevent p{position:absolute;left:42px;top:90px;width:490px;font-size:11.5px;line-height:20px}

/* partners */
.partner{position:absolute;top:3838px;width:70px;height:70px;border-radius:50%;background:#eceef1}

/* contact */
.contact{position:absolute;top:3988px;left:0;width:1200px;height:612px;background:linear-gradient(180deg,#143a62 0%,#1d4d7c 60%,#173f69 100%)}
.contact-title{position:absolute;left:0;top:4050px;width:1200px;text-align:center;color:var(--white);font-size:30px;font-weight:700}
.field{position:absolute;left:137px;width:453px;height:46px;border:1px solid rgba(255,255,255,.5);border-radius:2px;background:rgba(255,255,255,.04);color:var(--white);font-size:14px;padding:13px 16px}
.contact-brand{position:absolute;left:660px;top:4150px;display:flex;align-items:center;gap:10px;color:var(--white);font-family:"Roboto",sans-serif;font-weight:900;font-size:22px;line-height:1}
.contact-brand .dot{width:14px;height:14px;border-radius:50%;background:var(--white)}
.contact-brand small{display:block;font-size:11px;font-weight:500;margin-top:4px;letter-spacing:1px}
.contact-info{position:absolute;left:662px;top:4238px;width:260px;color:var(--white)}
.contact-info h4{font-size:18px;font-weight:700;margin-bottom:18px}
.contact-row{display:flex;gap:16px;font-size:13.5px;line-height:24px;margin-bottom:20px}
.contact-row svg{flex:none;margin-top:5px}

/* footer */
.footer-nav{position:absolute;top:4630px;left:346px;display:flex}
.footer-nav a{font-size:15px;color:var(--ink);text-decoration:none;margin-right:33px}
.footer-nav a.active{color:var(--red);font-weight:700}
.social{position:absolute;top:4674px;width:42px;height:42px;border-radius:50%;background:var(--red)}
.copyright{position:absolute;top:4740px;left:0;width:1200px;text-align:center;font-size:13px;color:var(--ink)}
</style>
</head>
<body>

<header class="site-header">
  <div class="brand"><span class="dot"></span><div>Tidewell Search<small>DIVE TEAM</small></div></div>
  <nav class="main-nav">
    <a class="active" href="#">Home</a><a href="#">About Us</a><a href="#">Services</a><a href="#">Team</a><a href="#">Donate</a><a href="#">Contact Us</a>
  </nav>
  <a class="btn btn-red" href="#" style="left:900px;top:38px;width:162px;height:42px">Get a Quote</a>
</header>

<section class="hero">
  <svg class="abs" width="1200" height="540" viewBox="0 0 1200 540" role="img" aria-label="Scuba diver ascending through deep blue water toward the light">
    <defs>
      <linearGradient id="heroGrad" x1="0" y1="0" x2="1" y2="0.6">
        <stop offset="0" stop-color="#1a0608"/>
        <stop offset="0.35" stop-color="#0a2448"/>
        <stop offset="0.7" stop-color="#134f95"/>
        <stop offset="1" stop-color="#2a7fd0"/>
      </linearGradient>
    </defs>
    <path d="M0 0H1200V449C1000 520 780 545 600 533C400 520 150 470 0 422Z" fill="url(#heroGrad)"/>
  </svg>
  <div class="hero-text">
    <h1>Bringing <span class="hl">Hope to<br>the Surface</span></h1>
    <p>Recovery and Support for Drowning<br>Victims and Their Families</p>
  </div>
  <a class="btn btn-red" href="#" style="left:193px;top:300px;width:162px;height:40px">Get Started</a>
  <a class="btn btn-outline" href="#" style="left:370px;top:300px;width:162px;height:40px">Donate Now</a>
</section>

<div class="about-bg"></div>
<a class="scroll-btn" href="#" aria-label="Scroll down">
  <svg width="20" height="12" viewBox="0 0 20 12"><path d="M2 2l8 8 8-8" fill="none" stroke="#123557" stroke-width="3"/></svg>
</a>

<section class="about">
  <div class="placeholder" role="img" aria-label="Divers wading into the sea at sunset" style="left:140px;top:765px;width:448px;height:288px;border:4px solid #fff;box-shadow:0 6px 18px rgba(0,0,0,.25);background:linear-gradient(180deg,#e2501c 0%,#f28b2c 35%,#7a2410 70%,#2b0f08 100%)"></div>
  <h2 class="about-title"><span class="hl">About Tidewell Search</span><br>Dive Team</h2>
  <div class="about-line"></div>
  <p class="about-text">Recovery services for drowning victims encompass a series of actions, protocols, and support systems aimed at locating, retrieving, and providing assistance to victims of drowning incidents, as well as helping their families cope with the emotional and psychological aftermath. These services can be broken down into several key areas</p>
  <a class="btn btn-red" href="#" style="left:613px;top:1027px;width:160px;height:40px">Get Started</a>
</section>

<section class="stages">
  <p class="abs" style="left:0;top:1174px;width:1200px;text-align:center;font-size:14px;font-weight:600">The 4 Stages of drowning Victim search</p>
  <h2 class="section-title" style="top:1200px"><span class="hl">Search and</span> Rescue Operations</h2>
  <div class="divider" style="top:1270px"></div>

  <div class="stage-dash" style="left:359px;width:50px"></div>
  <div class="stage-dash" style="left:577px;width:50px"></div>
  <div class="stage-dash" style="left:794px;width:50px"></div>

  <div class="stage" style="left:191px">
    <div class="ring"><div><svg width="64" height="58" viewBox="0 0 64 58"><path d="M32 3L62 55H2Z" fill="#fff"/><rect x="29" y="20" width="6" height="20" fill="#c1080f"/><rect x="29" y="44" width="6" height="6" fill="#c1080f"/></svg></div></div>
    <h4>First Response</h4>
  </div>
  <div class="stage" style="left:409px">
    <div class="ring"><div><svg width="68" height="58" viewBox="0 0 68 58"><rect x="6" y="4" width="22" height="22" rx="4" fill="#fff"/><rect x="40" y="4" width="22" height="22" rx="4" fill="#fff"/><rect x="2" y="22" width="28" height="34" rx="6" fill="#fff"/><rect x="38" y="22" width="28" height="34" rx="6" fill="#fff"/><rect x="28" y="16" width="12" height="18" fill="#fff"/></svg></div></div>
    <h4>Watchfull<br>stand by</h4>
  </div>
  <div class="stage" style="left:626px">
    <div class="ring"><div><svg width="60" height="60" viewBox="0 0 60 60"><circle cx="24" cy="24" r="17" fill="none" stroke="#fff" stroke-width="6"/><path d="M37 37L56 56" stroke="#fff" stroke-width="8" stroke-linecap="round"/></svg></div></div>
    <h4>Active Search</h4>
  </div>
  <div class="stage" style="left:843px">
    <div class="ring"><div><svg width="70" height="50" viewBox="0 0 70 50" fill="none" stroke="#fff" stroke-width="6" stroke-linecap="round"><path d="M4 10q8-8 16 0t16 0 16 0 14 0"/><path d="M4 25q8-8 16 0t16 0 16 0 14 0"/><path d="M4 40q8-8 16 0t16 0 16 0 14 0"/></svg></div></div>
    <h4>Disengaged<br>waiting</h4>
  </div>

  <div class="abs" style="left:540px;top:1598px;width:120px;height:2px;background:#555"></div>
  <div class="abs" style="left:599px;top:1598px;width:2px;height:205px;background:#555"></div>

  <div class="team-type" style="left:140px">
    <h3>Coast Guard, Fire, and Rescue Teams</h3>
    <p>These agencies are typically involved in searching for drowning victims in bodies of water. They use specialized equipment, such as boats, drones, underwater sonar, and divers, to locate victims who are missing or presumed drowned.</p>
  </div>
  <div class="team-type" style="left:660px">
    <h3>Community Volunteers</h3>
    <p>In some cases, local communities or trained volunteer rescue teams assist in locating victims, especially in rural or less-accessible areas.</p>
  </div>
  <a class="btn btn-red" href="#" style="left:518px;top:1798px;width:164px;height:40px">Get Started</a>

  <h2 class="section-title" style="top:1880px;color:var(--red)">Services</h2>
  <div class="divider" style="top:1953px"></div>
</section>

<section class="services">
  <div class="services-band"></div>
  <svg class="abs" style="left:0;top:2000px" width="600" height="568" viewBox="0 0 600 568" role="img" aria-label="Divers swimming in blue open water">
    <defs><linearGradient id="svcGrad" x1="0" y1="0" x2="1" y2="1"><stop offset="0" stop-color="#2c6aa5"/><stop offset="1" stop-color="#163d68"/></linearGradient></defs>
    <path d="M0 0H555L598 568H0Z" fill="url(#svcGrad)"/>
  </svg>
  <h2 class="services-heading">Medical and<small>Psychological Support</small></h2>
  <div class="services-list">
    <div class="service-item"><span class="plus">+</span><h3>Resuscitation</h3><p>If a victim is found alive and requires immediate medical attention, CPR and other emergency medical procedures may be carried out to restore breathing and circulation.</p></div>
    <div class="service-item"><span class="plus">+</span><h3>Psychological Counseling</h3><p>For families and loved ones, counseling services may be available to help them cope with the trauma of the drowning incident. Grief counseling, support groups, and therapy can assist in processing the emotional pain of losing a loved one.</p></div>
  </div>
  <a class="btn btn-red" href="#" style="left:182px;top:2420px;width:164px;height:38px">Learn more</a>
  <div class="placeholder" role="img" aria-label="Cupped hands holding a paper cut-out family on a wooden desk" style="left:613px;top:2180px;width:448px;height:285px;border:4px solid #fff;box-shadow:0 6px 18px rgba(0,0,0,.2);background:linear-gradient(135deg,#6a5c4f 0%,#d9a88c 45%,#b07a62 60%,#5b4e44 100%)"></div>
</section>

<section class="team">
  <div class="team-band"></div>
  <h2 class="section-title" style="top:2630px;color:var(--white)">Our Team</h2>
  <div class="divider" style="top:2700px;background:#fff"></div>
  <style>.team .divider::after{background:#fff}</style>
  <div class="team-card" role="img" aria-label="Portrait of team member James" style="left:135px;background:linear-gradient(180deg,#dcdcdc,#9a9a9a)">
    <div class="team-label"><h4>James</h4><p>Diver team member</p></div>
  </div>
  <div class="team-card" role="img" aria-label="Portrait of a team member" style="left:373px;background:linear-gradient(180deg,#f4f1ec,#d8a24a)"></div>
  <div class="team-card" role="img" aria-label="Portrait of a team member" style="left:610px;background:linear-gradient(180deg,#f0f0f0,#8fb8df)"></div>
  <div class="team-card" role="img" aria-label="Portrait of a team member" style="left:847px;background:linear-gradient(180deg,#f2f2f2,#4b7fc2)"></div>
  <div class="team-dots"><span></span><span></span><span></span></div>
</section>

<section class="reunite">
  <h2 class="reunite-title">Reuniting<small>Loved Ones</small></h2>
  <div class="reunite-line"></div>
  <p class="reunite-text">Lorem ipsum dolor sit amet, consectetur adipiscing elit, sed do eiusmod tempor incididunt ut labore et dolore magna aliqua. Quis ipsum suspendisse ultrices gravida. Risus commodo viverra maecenas accumsan lacus vel facilisis.</p>
  <article class="info-card" role="img" aria-label="Family comforting each other, dark blue tone" style="left:371px;background:linear-gradient(180deg,#3f6a92 0%,#1d4468 60%,#142f4c 100%)">
    <div class="copy" style="top:48px"><h3>Family Notification</h3><p>When a drowning victim is located, authorities will work to notify family members in a sensitive and timely manner. This is a critical component of recovery services, ensuring families are informed about the situation and can begin to process the event.</p></div>
  </article>
  <article class="info-card" role="img" aria-label="Man sitting in quiet reflection, dark blue tone" style="left:721px;background:linear-gradient(180deg,#51708c 0%,#243f5c 55%,#142f4c 100%)">
    <div class="copy" style="top:105px"><h3>Memorial Services</h3><p>In the event of a fatal drowning, services may include funeral or memorial arrangements to allow families and friends to honor the deceased.</p></div>
  </article>
</section>

<section class="prevent" role="img" aria-label="Diver in mask and breathing gear beneath the surface, red tone" style="background:linear-gradient(90deg,#c1080f 0%,#c1080f 50%,#7a0408 72%,#b5141a 100%)">
  <h3>Preventative Education and Awareness</h3>
  <p><strong>Drowning Prevention Programs :</strong> As part of recovery services, there is often a focus on education and awareness campaigns that inform the public about water safety, swimming skills, and how to prevent drowning incidents in the future.</p>
  <a class="btn btn-black" href="#" style="left:707px;top:70px;width:162px;height:39px">Donate Now</a>
</section>

<section class="partners">
  <h2 class="section-title" style="top:3720px;font-size:30px"><span class="hl">Partner Agencies &amp;</span> Other Organisations</h2>
  <div class="divider" style="top:3792px"></div>
  <div class="partner" style="left:102px"></div>
  <div class="partner" style="left:277px"></div>
  <div class="partner" style="left:467px"></div>
  <div class="partner" style="left:653px"></div>
  <div class="partner" style="left:845px"></div>
  <div class="partner" style="left:1033px"></div>
</section>

<section>
  <div class="contact"></div>
  <h2 class="contact-title">Contact Us</h2>
  <div class="abs" style="left:495px;top:4098px;width:210px;height:2px;background:var(--red)"></div>
  <div class="abs" style="left:594px;top:4093px;width:12px;height:12px;background:var(--red);transform:rotate(45deg)"></div>
  <div class="field" style="top:4150px">Name</div>
  <div class="field" style="top:4222px">Email</div>
  <div class="field" style="top:4295px">Phone</div>
  <div class="field" style="top:4365px;height:125px">Message</div>
  <a class="btn btn-black" href="#" style="left:140px;top:4515px;width:130px;height:40px">Submit</a>

  <div class="contact-brand"><span class="dot"></span><div>Tidewell Search<small>DIVE TEAM</small></div></div>
  <div class="contact-info">
    <h4>Address</h4>
    <div class="contact-row"><svg width="14" height="16" viewBox="0 0 14 16"><path d="M7 0a6 6 0 0 1 6 6c0 4-6 10-6 10S1 10 1 6a6 6 0 0 1 6-6z" fill="#fff"/><circle cx="7" cy="6" r="2.2" fill="#1d4d7c"/></svg><span>#123 , Lorium ipsum<br>dolor amit, city name,<br>country.</span></div>
    <div class="contact-row"><svg width="14" height="14" viewBox="0 0 14 14"><path d="M3 0l3 3-2 2c1 2 3 4 5 5l2-2 3 3-2 3C6 14 0 8 0 2z" fill="#fff"/></svg><span>1800 555 0142</span></div>
    <div class="contact-row"><svg width="14" height="11" viewBox="0 0 14 11"><rect width="14" height="11" rx="1" fill="#fff"/><path d="M1 1l6 5 6-5" fill="none" stroke="#1d4d7c" stroke-width="1.5"/></svg><span>info@tidewellsearch.org</span></div>
  </div>
</section>

<footer>
  <nav class="footer-nav">
    <a class="active" href="#">Home</a><a href="#">About Us</a><a href="#">Services</a><a href="#">Team</a><a href="#">Donate</a><a href="#">Contact Us</a>
  </nav>
  <a class="social" href="#" aria-label="Social profile one" style="left:516px"></a>
  <a class="social" href="#" aria-label="Social profile two" style="left:579px"></a>
  <a class="social" href="#" aria-label="Social profile three" style="left:642px"></a>
  <p class="copyright">©2025 &nbsp;|&nbsp; www.tidewellsearch.org</p>
</footer>

</body>
</html>
```